Australian Recruitment Agency Flyer

We are looking for a 1 page flyer to promote our recruitment company. We would like this to have a corporate look.

Attached is a word document with the content we would like included in the flyer.

I have also attached some of our clients logos to be included in the flyer

Target Market(s)

Professional organisations looking to hire new staff

Industry/Entity Type

It Company

Colors
85abd2
3176b5
31b7a3
d2a4cc
e667a6
b768aa
876aae
3276b5
f04a50

Requirements
Must have
• Must have the content that we have include on a word document in the design brief.

```html
<!DOCTYPE html>
<html lang="en">
<head>
<meta charset="utf-8">
<title>TalentBridge – Human Resources &amp; Recruitment</title>
<link href="https://fonts.googleapis.com/css2?family=Montserrat:wght@600;700&family=Roboto+Condensed:ital,wght@0,400;0,700;1,700&family=Roboto:wght@400;700&display=swap" rel="stylesheet">
<style>
  :root {
    --sky: #85abd2;
    --blue: #3176b5;
    --teal: #31b7a3;
    --lilac: #d2a4cc;
    --pink: #e667a6;
    --orchid: #b768aa;
    --violet: #876aae;
    --red: #f04a50;
    --ink: #3b3f47;
    --footer: #3a3f48;
    --white: #ffffff;
  }
  * { margin: 0; padding: 0; box-sizing: border-box; }
  html, body { width: 927px; height: 1200px; overflow: hidden; background: #fff; }
  .flyer {
    position: relative; width: 927px; height: 1200px; overflow: hidden;
    font-family: "Roboto Condensed", "Arial Narrow", sans-serif; color: var(--ink);
  }
  .photo {
    position: absolute; left: 0; top: 90px; width: 927px; height: 900px;
    background: linear-gradient(160deg, #e9eef2 0%, #c9d4dc 35%, #d8c8b4 60%, #b9a48c 100%);
  }
  .shapes { position: absolute; inset: 0; width: 927px; height: 1200px; }
  .brand { position: absolute; left: 34px; top: 34px; display: flex; align-items: center; gap: 22px; }
  .brand-square { width: 118px; height: 118px; background: var(--violet); }
  .brand-name { font-family: "Montserrat", sans-serif; font-weight: 700; font-size: 60px; color: var(--ink); letter-spacing: -1px; line-height: 1; }
  .brand-tag { font-family: "Roboto", sans-serif; font-size: 19px; color: var(--ink); margin-top: 14px; margin-left: 4px; }
  .experience {
    position: absolute; left: 580px; top: 351px; width: 347px; height: 222px;
    color: var(--white); text-align: right; padding: 16px 20px 0 0; font-weight: 700; line-height: 1.02;
  }
  .experience .lead { font-size: 31px; }
  .experience .years { font-size: 68px; line-height: 0.98; }
  .experience .rest { font-size: 31px; }
  .industries { position: absolute; left: 566px; top: 646px; width: 340px; color: var(--white); }
  .industries h2 { font-size: 30px; font-weight: 700; letter-spacing: 0.5px; margin-bottom: 20px; }
  .industries ul { list-style: none; margin-left: 22px; }
  .industries li { font-size: 23px; display: flex; align-items: center; gap: 8px; height: 33.5px; }
  .industries svg { width: 18px; height: 18px; flex: none; }
  .about { position: absolute; left: 22px; top: 776px; width: 520px; }
  .about h2 { font-size: 31px; font-weight: 700; color: var(--violet); letter-spacing: 0.5px; border-bottom: 2px solid var(--lilac); padding-bottom: 4px; width: 225px; }
  .about p { font-family: "Roboto", sans-serif; font-size: 18px; line-height: 1.3; margin-top: 16px; }
  .about em { color: var(--blue); font-weight: 700; font-size: 20px; }
  .about .cta { font-family: "Roboto Condensed", "Arial Narrow", sans-serif; font-size: 28px; line-height: 1.2; margin-top: 26px; color: var(--ink); }
  .clients { position: absolute; left: 22px; top: 1032px; display: flex; gap: 6px; }
  .client {
    height: 54px; width: 70px; background: #fff; box-shadow: 0 1px 3px rgba(0,0,0,.3);
    display: flex; align-items: center; justify-content: center;
    font-family: "Roboto Condensed", sans-serif; font-size: 13px; font-weight: 700; color: var(--ink);
  }
  .footer {
    position: absolute; left: 0; top: 1103px; width: 927px; height: 97px; background: var(--footer);
    color: var(--white); display: flex; align-items: center; padding-left: 34px;
  }
  .call { display: flex; flex-direction: column; line-height: 1; }
  .call .label { font-size: 21px; display: flex; align-items: center; gap: 8px; margin-left: 36px; }
  .call .number { font-size: 35px; font-weight: 700; margin-top: 6px; }
  .divider { width: 2px; height: 44px; background: var(--white); margin: 18px 14px 0; }
  .web { display: flex; flex-direction: column; align-items: center; font-size: 25px; line-height: 1; }
  .web svg { margin-bottom: 8px; }
  .teal-panel {
    position: absolute; left: 576px; top: 868px; width: 351px; height: 306px; background: var(--teal);
    clip-path: polygon(0 26px, 100% 0, 100% 100%, 0 100%);
  }
  .testimonial { position: absolute; left: 596px; top: 908px; width: 315px; color: var(--white); }
  .testimonial blockquote { font-size: 21px; line-height: 1.26; }
  .testimonial .author { text-align: right; margin-top: 14px; color: #2d3340; padding-right: 6px; }
  .author .name, .author .role { font-size: 24px; font-weight: 700; font-style: italic; line-height: 1.05; }
  .author .company { font-size: 17px; margin-top: 3px; }
</style>
</head>
<body>
<div class="flyer">
  <div class="photo" role="img" aria-label="Photo of a smiling interview panel of three people seated at a table facing a candidate"></div>

  <svg class="shapes" viewBox="0 0 927 1200" aria-hidden="true">
    <polygon points="0,0 927,0 927,60 0,220" fill="#ffffff"/>
    <polygon points="690,0 927,0 927,272" fill="var(--red)"/>
    <polygon points="596,351 927,351 927,573 580,573 580,366" fill="var(--blue)" opacity="0.92"/>
    <polygon points="0,735 560,655 560,1136 0,1136" fill="#ffffff"/>
    <polygon points="566,636 909,636 909,866 541,879 541,660" fill="var(--orchid)"/>
  </svg>

  <header class="brand">
    <div class="brand-square"></div>
    <div>
      <div class="brand-name">TalentBridge</div>
      <div class="brand-tag">Human Resources &amp; Recruitment</div>
    </div>
  </header>

  <section class="experience">
    <div class="lead">We have over</div>
    <div class="years">20 years</div>
    <div class="rest">of experience<br>helping companies<br>hire amazing talent</div>
  </section>

  <section class="industries">
    <h2>INDUSTRIES WE SERVE</h2>
    <ul>
      <li><svg viewBox="0 0 18 18"><circle cx="9" cy="9" r="8" fill="#fff"/><path d="M9 4 L14 9 H11 V14 H7 V9 H4 Z" fill="var(--orchid)"/></svg>Mining and Oil &amp; Gas</li>
      <li><svg viewBox="0 0 18 18"><circle cx="9" cy="9" r="8" fill="#fff"/><path d="M9 4 L14 9 H11 V14 H7 V9 H4 Z" fill="var(--orchid)"/></svg>Accounting &amp; Finance</li>
      <li><svg viewBox="0 0 18 18"><circle cx="9" cy="9" r="8" fill="#fff"/><path d="M9 4 L14 9 H11 V14 H7 V9 H4 Z" fill="var(--orchid)"/></svg>Sales &amp; Marketing</li>
      <li><svg viewBox="0 0 18 18"><circle cx="9" cy="9" r="8" fill="#fff"/><path d="M9 4 L14 9 H11 V14 H7 V9 H4 Z" fill="var(--orchid)"/></svg>IT &amp; Communications</li>
      <li><svg viewBox="0 0 18 18"><circle cx="9" cy="9" r="8" fill="#fff"/><path d="M9 4 L14 9 H11 V14 H7 V9 H4 Z" fill="var(--orchid)"/></svg>Government &amp; Not for Profit</li>
    </ul>
  </section>

  <section class="about">
    <h2>WHAT WE DO</h2>
    <p>We aren’t a recruitment agency, we are an extension of your team. We become your very own <em>HR &amp; Recruitment</em> department to be called upon as and when needed.</p>
    <p class="cta">Start a conversation today and see why these companies turn to us time and time again</p>
  </section>

  <div class="clients">
    <div class="client">Vanta</div>
    <div class="client">Orbis</div>
    <div class="client">Ridgeway</div>
    <div class="client">Saltlake</div>
    <div class="client">Roadwise</div>
    <div class="client">Harbourline</div>
    <div class="client">Keystone</div>
  </div>

  <footer class="footer">
    <div class="call">
      <span class="label"><svg width="20" height="20" viewBox="0 0 24 24"><path d="M6.6 10.8c1.4 2.8 3.8 5.1 6.6 6.6l2.2-2.2c.3-.3.7-.4 1-.2 1.1.4 2.3.6 3.6.6.6 0 1 .4 1 1V20c0 .6-.4 1-1 1C10.6 21 3 13.4 3 4c0-.6.4-1 1-1h3.5c.6 0 1 .4 1 1 0 1.3.2 2.5.6 3.6.1.3 0 .7-.2 1z" fill="#fff"/></svg>Call Now</span>
      <span class="number">1300 555 010</span>
    </div>
    <div class="divider"></div>
    <div class="web">
      <svg width="22" height="22" viewBox="0 0 24 24" fill="none" stroke="#fff" stroke-width="2"><circle cx="12" cy="12" r="10"/><ellipse cx="12" cy="12" rx="4.5" ry="10"/><line x1="2" y1="12" x2="22" y2="12"/></svg>
      <span>www.talentbridge.example</span>
    </div>
  </footer>

  <div class="teal-panel"></div>
  <section class="testimonial">
    <blockquote>“TalentBridge really delivered on their promise and far exceeded our expectations. Their fixed fee model saved us thousands”</blockquote>
    <div class="author">
      <div class="name">Daniel Morrow</div>
      <div class="role">General Manager</div>
      <div class="company">Harbourline Financial Services</div>
    </div>
  </section>
</div>
</body>
</html>
```